Plimora

We need a design for a mobile app (Android & iOS) with the following features:
- Recommend other applications based on different criteria, such as similar applications, hot apps, apps installed by friends and so on.
- Recommend a featured app everyday.
- List installed apps on the device.
- List harmful or malicious installed apps on the device
- List hot apps according to the more used apps by the comunity or the user's friends
- Profiles: Save the list of apps installed on the device as a list to allow the user to restore them on other devices.

Industry/Entity Type

Android

Requirements
Must have
• Find attached to this project a mockup of the screen elements desired.
To put it in a nutshell, the main elements are:
- Main Menu: A main menu to access the other modules of the app

- Recommended Apps: List of apps recommended, each app will display: icon, title, price, the reason(s) why it was recommended (can be expandable if takes too much room), a button to install and a button to ignore the advice.

- Application of the day: A screen that contains the icon of the app, its rating, some screenshots, a short description or promotional text, and a button to install the app. It must be also available a way to display the history and see the recommended applications the previous days.

- Installed Apps: A list with the apps on the device. It will show the app's icon, name, package, size and a button to share the app.

- Harmful apps: List of dangerous apps found on the device. It will show the icon of the app and the name. A visual and textual indicator to measure the dangerous, and the reasons of the report. It will also includes a button to ignore the advice and another one to uninstall the application.

- Login/My account: These screens will be used to login and manage the account. The account management options are listed on the attached document.

- Profiles: The design must include the proper screens and dialogs to: save a profile, restore a profile (install the missing apps on the device), show the apps saved on the profile.

- Hot Apps: The app must allow to filter between the hot apps and the hot apps installed by the user's friends. For each app, must show: the icon, name and a trending indicator in order to say if the app is winning or losing popularity

- Miscellaneous: Other features required:
+ Login screen: The login is made in two steps. First, the user introduce their email. If the email is already registered, enters the password. Otherwise, register a new account introducing a password twice (password + repeat password, please check the attached file for more info).
+ Password recovery and password change screens
+ Loading splash (shown at the start of the application for 2-4 seconds)
+ A proper layout to inform about errors / messages in empty lists, (for example if no harmful apps where found).
+ A proper layout for loading process, for example when scanning for harmful apps.
+ Vectorial App Icon: At least one icon for the app (512 x512 px)
+ Vectorial Featured (1024x500 px) and Promo banners (180x120 px) for Vexari Shop.
+ For the UI elements like buttons or checkboxes is required the following status: normal, pressed, disabled and focused.
Nice to have
• Examples of apps with nice designs:

Trendle: https://shop.vexari.example/apps/details?id=com.trendle
Quill Digest: https://shop.vexari.example/apps/details?id=com.borvik.quill
ORB Coastal Terminals: https://tunes.halvexo.example/es/app/orb-coastal-terminals/id871402965?mt=8
Should not have
• The app should not have garish or poorly contrasted colors and icons.

```html
<!DOCTYPE html>
<html lang="en">
<head>
<meta charset="utf-8">
<title>Plimora – App of the day</title>
<link rel="stylesheet" href="https://fonts.googleapis.com/css2?family=Quicksand:wght@400;500&display=swap">
<style>
  :root{
    --stage-light:#ececec;
    --stage-dark:#a9a9a9;
    --panel-dark:#2e2e2e;
    --teal-light:#11a58f;
    --teal-mid:#0c8a79;
    --teal-deep:#075e55;
    --teal-night:#0b3f3a;
    --header-dark-top:#404040;
    --header-dark-bottom:#232323;
    --ring-idle:#464646;
    --white:#ffffff;
    --chip:#d9dadb;
    --bar:#9a9a9a;
    --ink:#1e1e1e;
  }
  *{box-sizing:border-box;margin:0;padding:0}
  html,body{width:1200px;height:684px;overflow:hidden}
  body{
    font-family:"Quicksand",sans-serif;
    background:radial-gradient(ellipse at 50% 45%,var(--stage-light) 0%,#d4d4d4 55%,var(--stage-dark) 100%);
  }
  .stage{position:relative;width:1182px;height:674px;transform:scale(1.0152,1.0148);transform-origin:0 0}
  .screen{position:absolute;width:375px}
  .screen--loading-a{left:8px;top:12px}
  .screen--loading-b{left:394px;top:12px}
  .screen--featured{left:800px;top:14px}

  .app-bar{
    height:47px;display:flex;align-items:center;justify-content:space-between;padding:0 9px;
    background:linear-gradient(var(--teal-light),var(--teal-deep));color:var(--white);
  }
  .app-bar--dark{height:48px;background:linear-gradient(var(--header-dark-top),var(--header-dark-bottom))}
  .app-bar__title{font-size:25px;font-weight:400;letter-spacing:.2px}
  .app-bar svg{width:34px;height:34px;display:block}

  .loading{
    margin-top:4px;height:592px;background:var(--panel-dark);position:relative;
  }
  .progress-ring{position:absolute;left:90px;top:155px;width:210px;height:210px}
  .progress-ring__value{
    position:absolute;left:0;top:0;width:100%;height:100%;display:flex;align-items:center;justify-content:center;
    color:var(--white);font-size:86px;font-weight:400;
    text-shadow:0 0 10px rgba(255,255,255,.55);
  }
  .loading__label{position:absolute;top:412px;width:100%;text-align:center;color:var(--white);font-size:19px}

  .featured{
    height:594px;
    background:linear-gradient(#262626 0px,#262626 22px,#1d3a37 80px,#0f6f64 180px,var(--teal-mid) 300px,#0c6c61 450px,var(--teal-night) 594px);
    position:relative;color:var(--white);
  }
  .rule{position:absolute;left:0;width:100%;height:2px;background:linear-gradient(90deg,transparent,#5b5b5b 15%,#6e6e6e 50%,#5b5b5b 85%,transparent)}
  .app-head{position:absolute;top:22px;left:0;width:100%;height:70px}
  .app-head__icon{position:absolute;left:46px;top:10px;width:52px;height:52px;border-radius:7px;background:#e4e5e7}
  .app-head__name{position:absolute;left:124px;top:21px;font-size:21px}
  .install-btn{
    position:absolute;left:275px;top:22px;width:78px;height:27px;border-radius:4px;
    border:2px solid #cde7e3;background:linear-gradient(var(--teal-light),var(--teal-deep));
    display:flex;align-items:center;gap:9px;padding-left:8px;font-size:12px;color:var(--white);
  }
  .install-btn svg{width:14px;height:16px}
  .rating-card{
    position:absolute;left:54px;top:105px;width:84px;height:84px;border-radius:10px;background:var(--chip);
    color:var(--ink);text-align:center;
  }
  .rating-card__score{font-size:33px;margin-top:12px;line-height:1}
  .rating-card__count{font-size:12px;margin-top:10px}
  .rating-bars{position:absolute;left:130px;top:110px;list-style:none}
  .rating-bars li{display:flex;align-items:center;height:14.8px;font-size:9.5px;color:#e8e8e8}
  .rating-bars span{width:80px;text-align:right;padding-right:4px}
  .rating-bars i{display:block;height:9px;border-radius:4px;background:var(--bar)}
  .shots{position:absolute;top:202px;left:15px;display:flex;gap:11px}
  .shot{width:110px;height:188px;border:2px solid var(--white)}
  .blurb{position:absolute;top:400px;left:20px;width:335px;text-align:center;font-size:13.4px;line-height:19.4px}
</style>
</head>
<body>
<div class="stage">

  <section class="screen screen--loading-a">
    <header class="app-bar">
      <svg viewBox="0 0 34 34" aria-label="Back"><circle cx="17" cy="17" r="15" fill="none" stroke="#fff" stroke-width="2.6"/><path d="M25 17H11M16 11l-6 6 6 6" fill="none" stroke="#fff" stroke-width="2.8" stroke-linecap="round" stroke-linejoin="round"/></svg>
      <h1 class="app-bar__title">App of the day</h1>
      <svg viewBox="0 0 34 34" aria-label="Settings"><circle cx="17" cy="17" r="15" fill="none" stroke="#fff" stroke-width="2.6"/><g fill="#fff"><circle cx="17" cy="17" r="7"/><rect x="15.2" y="6.5" width="3.6" height="21" rx="1"/><rect x="15.2" y="6.5" width="3.6" height="21" rx="1" transform="rotate(45 17 17)"/><rect x="15.2" y="6.5" width="3.6" height="21" rx="1" transform="rotate(90 17 17)"/><rect x="15.2" y="6.5" width="3.6" height="21" rx="1" transform="rotate(135 17 17)"/></g><circle cx="17" cy="17" r="3" fill="#0c8a79"/></svg>
    </header>
    <div class="loading">
      <div class="progress-ring">
        <svg viewBox="0 0 210 210" width="210" height="210">
          <defs><linearGradient id="segA" x1="0" y1="0" x2="1" y2="1"><stop offset="0" stop-color="#13a892"/><stop offset="1" stop-color="#07685d"/></linearGradient></defs>
          <g transform="rotate(-87.5 105 105)" fill="none" stroke-width="22">
            <circle cx="105" cy="105" r="91" stroke="var(--ring-idle)" stroke-dasharray="63.5 8"/>
            <circle cx="105" cy="105" r="91" stroke="url(#segA)" stroke-dasharray="63.5 8 63.5 436.8"/>
          </g>
        </svg>
        <div class="progress-ring__value">27</div>
      </div>
      <p class="loading__label">Loading application . . .</p>
    </div>
  </section>

  <section class="screen screen--loading-b">
    <header class="app-bar">
      <svg viewBox="0 0 34 34" aria-label="Back"><circle cx="17" cy="17" r="15" fill="none" stroke="#fff" stroke-width="2.6"/><path d="M25 17H11M16 11l-6 6 6 6" fill="none" stroke="#fff" stroke-width="2.8" stroke-linecap="round" stroke-linejoin="round"/></svg>
      <h1 class="app-bar__title">App of the day</h1>
      <svg viewBox="0 0 34 34" aria-label="Settings"><circle cx="17" cy="17" r="15" fill="none" stroke="#fff" stroke-width="2.6"/><g fill="#fff"><circle cx="17" cy="17" r="7"/><rect x="15.2" y="6.5" width="3.6" height="21" rx="1"/><rect x="15.2" y="6.5" width="3.6" height="21" rx="1" transform="rotate(45 17 17)"/><rect x="15.2" y="6.5" width="3.6" height="21" rx="1" transform="rotate(90 17 17)"/><rect x="15.2" y="6.5" width="3.6" height="21" rx="1" transform="rotate(135 17 17)"/></g><circle cx="17" cy="17" r="3" fill="#0c8a79"/></svg>
    </header>
    <div class="loading">
      <div class="progress-ring">
        <svg viewBox="0 0 210 210" width="210" height="210">
          <defs><linearGradient id="segB" x1="0" y1="0" x2="1" y2="1"><stop offset="0" stop-color="#13a892"/><stop offset="1" stop-color="#07685d"/></linearGradient></defs>
          <g transform="rotate(-87.5 105 105)" fill="none" stroke-width="22">
            <circle cx="105" cy="105" r="91" stroke="url(#segB)" stroke-dasharray="63.5 8"/>
          </g>
        </svg>
        <div class="progress-ring__value">98</div>
      </div>
      <p class="loading__label">Loading application . . .</p>
    </div>
  </section>

  <section class="screen screen--featured">
    <header class="app-bar app-bar--dark">
      <svg viewBox="0 0 34 34" aria-label="Back"><circle cx="17" cy="17" r="15" fill="none" stroke="#fff" stroke-width="2.6"/><path d="M25 17H11M16 11l-6 6 6 6" fill="none" stroke="#fff" stroke-width="2.8" stroke-linecap="round" stroke-linejoin="round"/></svg>
      <h1 class="app-bar__title">App of the day</h1>
      <svg viewBox="0 0 34 34" aria-label="Settings"><circle cx="17" cy="17" r="15" fill="none" stroke="#fff" stroke-width="2.6"/><g fill="#fff"><circle cx="17" cy="17" r="7"/><rect x="15.2" y="6.5" width="3.6" height="21" rx="1"/><rect x="15.2" y="6.5" width="3.6" height="21" rx="1" transform="rotate(45 17 17)"/><rect x="15.2" y="6.5" width="3.6" height="21" rx="1" transform="rotate(90 17 17)"/><rect x="15.2" y="6.5" width="3.6" height="21" rx="1" transform="rotate(135 17 17)"/></g><circle cx="17" cy="17" r="3" fill="#2a2a2a"/></svg>
    </header>
    <div class="featured">
      <div class="rule" style="top:20px"></div>
      <div class="rule" style="top:90px"></div>
      <div class="app-head">
        <div class="app-head__icon" role="img" aria-label="Featured app icon"></div>
        <h2 class="app-head__name">App name</h2>
        <div class="install-btn">
          <svg viewBox="0 0 14 16"><rect width="14" height="16" rx="2" fill="#9fe0d5"/><path d="M7 3v8M3.5 8 7 11.5 10.5 8" fill="none" stroke="#0a6e63" stroke-width="1.8" stroke-linecap="round"/></svg>
          Install
        </div>
      </div>
      <div class="rating-card">
        <p class="rating-card__score">4.5</p>
        <p class="rating-card__count">2.3k reviews</p>
      </div>
      <ul class="rating-bars">
        <li><span>5 stars &nbsp;(2001)</span><i style="width:98px"></i></li>
        <li><span>4 stars &nbsp;(50)</span><i style="width:20px"></i></li>
        <li><span>3 stars &nbsp;(10)</span><i style="width:20px"></i></li>
        <li><span>2 stars &nbsp;(05)</span><i style="width:20px"></i></li>
        <li><span>1 star &nbsp;(150)</span><i style="width:40px"></i></li>
      </ul>
      <div class="shots">
        <div class="shot" role="img" aria-label="App screenshot one"></div>
        <div class="shot" role="img" aria-label="App screenshot two"></div>
        <div class="shot" role="img" aria-label="App screenshot three"></div>
      </div>
      <p class="blurb">“Lorem ipsum dolor sit amet, consectetur adipisicing<br>elit do ” eiusmod tempor incididunt ut labore et<br>dolore magna aliqua. Ut enim ad minim veniam,<br>quis nostrud exercitation ullamco laboris nisi ut<br>aliquip ex ea commodo consequat. Duis aute irure<br>dolor in reprehenderit in voluptate velit esse cillum<br>dolore eu fugiat nulla pariatur. Excepteur sint occae-</p>
    </div>
  </section>

</div>
</body>
</html>
```